VELVET ORBITS - BOOK COVER

I have written a book called VELVET ORBIT - HOW TO CLIMB PAST EVERY LIMIT TO THE TOP RUNG. I need a front cover design for the book. The book cover needs to be intriguing for someone to pick it up and read the first couple of pages. I want people to think about ACHIEVING SUCCESS when they read this book.
PLEASE LOOK AT THE ATTACHMENT. THANKS!

Target Market(s)

males, entrepreneurs, small business owners, salespeople, corporate executives

Industry/Entity Type

Business

Logo Text

VELVET ORBITS

Logo styles of interest
Emblem Logo
Abstract Logo
Font styles to use
Serif
Sans Serif

Colors
ec1f27
000000
959595
ffffff

Requirements
Must have
• It has to have a "hurricane" feel to it with hurricane colors.
Nice to have
• I open to your ideas
Should not have
• no other colors except red, black, gray, white.

```html
<!DOCTYPE html>
<html lang="en">
<head>
<meta charset="utf-8">
<title>Velvet Orbits – Book Cover</title>
<link href="https://fonts.googleapis.com/css2?family=Open+Sans:wght@700&family=Teko:wght@400;500&display=swap" rel="stylesheet">
<style>
  :root {
    --red: #ec1f27;
    --black: #000000;
    --gray: #959595;
    --white: #ffffff;
    --steel-dark: #6f7780;
    --steel: #a3aab2;
    --steel-light: #d9dde1;
    --haze: #eef0f2;
    --suit: #262d3a;
  }
  * { margin: 0; padding: 0; box-sizing: border-box; }
  html, body { width: 856px; height: 1200px; overflow: hidden; background: var(--red); }
  .cover { position: relative; width: 856px; height: 1200px; background: var(--red); overflow: hidden; }
  .cover-photo {
    position: absolute; left: 0; top: 97px; width: 856px; height: 775px;
    background:
      radial-gradient(ellipse 190px 330px at 690px 560px, var(--suit) 0%, rgba(38,45,58,0.85) 45%, rgba(38,45,58,0) 100%),
      radial-gradient(ellipse 260px 420px at 120px 420px, rgba(111,119,128,0.9) 0%, rgba(111,119,128,0) 100%),
      radial-gradient(ellipse 220px 200px at 330px 600px, rgba(111,119,128,0.7) 0%, rgba(111,119,128,0) 100%),
      linear-gradient(160deg, var(--steel) 0%, var(--steel-light) 30%, var(--haze) 50%, var(--white) 62%, var(--steel-light) 100%);
  }
  .cover-shapes { position: absolute; inset: 0; width: 856px; height: 1200px; }
  .brand-mark {
    position: absolute; left: 36px; top: 392px;
    display: flex; align-items: center; gap: 14px;
    font-family: "Teko", sans-serif; font-weight: 500; font-size: 54px; line-height: 1;
    color: var(--black); letter-spacing: 1px;
  }
  .brand-mark__square { width: 44px; height: 44px; background: var(--black); margin-bottom: 8px; }
  .author {
    position: absolute; left: 34px; top: 764px;
    font-family: "Open Sans", sans-serif; font-weight: 700; font-size: 27px;
    color: var(--white); letter-spacing: 0.3px;
  }
  .title {
    position: absolute; left: 34px; top: 862px;
    font-family: "Teko", sans-serif; font-weight: 400; font-size: 108px; line-height: 1;
    color: var(--white); letter-spacing: 2px;
  }
  .subtitle {
    position: absolute; left: 34px; top: 1058px;
    font-family: "Teko", sans-serif; font-weight: 400; font-size: 50px; line-height: 48px;
    color: var(--white); letter-spacing: 0.5px;
  }
  .social-link {
    position: absolute; right: 34px; top: 1108px;
    font-family: "Teko", sans-serif; font-weight: 500; font-size: 40px; line-height: 1;
    color: var(--white);
  }
</style>
</head>
<body>
<main class="cover">
  <div class="cover-photo" role="img" aria-label="Photograph of a confident businessman in a dark suit, arms crossed, standing beneath white modern architecture and glass towers"></div>

  <svg class="cover-shapes" viewBox="0 0 856 1200" aria-hidden="true">
    <rect x="0" y="0" width="856" height="97" fill="var(--red)"/>
    <polygon points="0,97 345,97 355,108 0,108" fill="var(--black)"/>
    <polygon points="256,108 430,108 449,133 272,133" fill="var(--gray)"/>
    <polygon points="420,85 856,85 856,133 440,133" fill="var(--black)"/>
    <polygon points="362,133 856,133 856,193 690,193 642,145 372,145" fill="var(--red)"/>

    <g fill="var(--red)">
      <polygon points="0,150 0,170 82,252 102,252"/>
      <polygon points="0,112 20,112 135,252 115,252"/>
      <polygon points="30,112 50,112 165,252 145,252"/>
      <polygon points="62,112 82,112 162,210 162,236"/>
    </g>

    <polygon points="0,697 170,697 212,742 0,742" fill="var(--black)"/>
    <rect x="0" y="742" width="230" height="10" fill="var(--gray)"/>
    <polygon points="0,755 440,755 470,782 470,810 0,810" fill="var(--red)"/>
    <polygon points="440,755 500,755 528,782 470,782" fill="var(--gray)"/>

    <polygon points="0,810 560,810 560,790 620,842 856,842 856,990 0,990" fill="var(--black)"/>

    <g fill="var(--red)">
      <polygon points="560,790 572,790 770,990 758,990"/>
      <polygon points="612,842 626,842 774,990 760,990"/>
      <polygon points="632,842 646,842 794,990 780,990"/>
      <polygon points="652,842 666,842 814,990 800,990"/>
      <polygon points="672,842 686,842 834,990 820,990"/>
      <polygon points="692,842 706,842 854,990 840,990"/>
      <polygon points="712,842 726,842 856,972 856,986"/>
    </g>
    <g fill="var(--gray)">
      <polygon points="700,757 716,757 856,955 856,978"/>
      <polygon points="730,757 746,757 856,912 856,935"/>
      <polygon points="760,757 776,757 856,870 856,892"/>
      <polygon points="790,757 806,757 856,828 856,850"/>
    </g>
  </svg>

  <div class="brand-mark"><span class="brand-mark__square"></span>VELVET ORBITS</div>
  <p class="author">BY CAL WRENFIELD</p>
  <h1 class="title">VELVET ORBITS</h1>
  <p class="subtitle">HOW TO CLIMB PAST EVERY LIMIT<br>TO THE TOP RUNG</p>
  <p class="social-link">ORBITLINK</p>
</main>
</body>
</html>
```